Business Card Design Project

We need a business card to reflect the design of our website - just so it all ties in - it has a retro feel and can be found at http://www.velorasoulpair.com
We will need our phone 0437 215 964
Web address, and email velorapair@fernmail.com included
Our catch cry is "Classic Cocktail Music"
Perfect Live Music for Private & Corporate Events, Weddings and Dinner Music
Our names should be included :-
Maribel Thorne / piano & Dennis Holloway / bass
I am now also including our logo so that it can be included (in part or whole) somehow in the design
My partner thinks we should include our logo in some form in the design of the card - i will attach this here for you. I will attach eps but if you prefer another format please let me know
Regards
Mari

```html
<!DOCTYPE html>
<html lang="en">
<head>
<meta charset="utf-8">
<title>Velora Pair – Business Card</title>
<link rel="stylesheet" href="https://fonts.googleapis.com/css2?family=Josefin+Sans:wght@400;600&family=Righteous&family=Jura:wght@400;500&family=EB+Garamond&display=swap">
<style>
  :root {
    --page: #f5f8f9;
    --teal: #78a9a9;
    --teal-light: #84b6b6;
    --teal-text: #79aaa8;
    --cream: #e8ddc2;
    --cream-band: #e6dbbd;
    --charcoal: #4a4a4a;
    --ink: #3a3a3a;
    --ink-soft: #4c4c4c;
  }
  * { margin: 0; padding: 0; box-sizing: border-box; }
  html, body { width: 1200px; height: 946px; overflow: hidden; }
  body {
    position: relative;
    background: linear-gradient(135deg, #f8fafb 0%, var(--page) 60%, #eef2f4 100%);
    font-family: "Jura", sans-serif;
  }
  .card {
    position: absolute;
    top: 140px;
    width: 425px;
    height: 660px;
    border-radius: 5px;
    overflow: hidden;
    box-shadow: 0 2px 6px rgba(0,0,0,0.18);
  }

  /* Front */
  .card-front { left: 92px; background: var(--teal); }
  .front-flap {
    position: absolute; inset: 0;
    width: 100%; height: 660px;
  }
  .badge {
    position: absolute;
    border-radius: 50%;
    background: var(--charcoal);
    color: var(--cream);
    display: flex; align-items: center; justify-content: center;
    text-align: center;
    font-family: "Josefin Sans", sans-serif;
    font-weight: 600;
    letter-spacing: 1px;
    line-height: 1.1;
  }
  .front-badge {
    left: 141px; top: 15px;
    width: 140px; height: 140px;
    font-size: 20px;
  }
  .front-name {
    position: absolute;
    left: 0; right: 0; top: 305px;
    text-align: center;
    font-family: "Josefin Sans", sans-serif;
    font-weight: 400;
    font-size: 46px;
    letter-spacing: 2px;
    color: var(--cream);
  }
  .front-footer {
    position: absolute;
    left: 0; right: 0; bottom: 0;
    height: 54px;
    background: var(--cream-band);
    display: flex; align-items: center; justify-content: center;
    font-family: "EB Garamond", serif;
    font-size: 18px;
    color: var(--ink-soft);
  }

  /* Back */
  .card-back { left: 636px; background: var(--cream); }
  .back-spine {
    position: absolute; left: 0; top: 0; bottom: 0;
    width: 16px; background: var(--teal);
  }
  .back-tab {
    position: absolute; left: 322px; top: 0;
    width: 76px; height: 76px;
  }
  .back-badge {
    left: 330px; top: 3px;
    width: 60px; height: 60px;
    font-size: 9px;
  }
  .tagline {
    position: absolute;
    left: 16px; right: 0; top: 164px;
    text-align: center;
    font-family: "Righteous", sans-serif;
    font-size: 24px;
    letter-spacing: 1px;
    color: var(--teal-text);
  }
  .person {
    position: absolute;
    right: 33px; top: 454px;
    text-align: right;
  }
  .person-name {
    font-family: "Jura", sans-serif;
    font-size: 18px;
    letter-spacing: 2px;
    color: var(--teal-text);
  }
  .person-role {
    font-family: "Jura", sans-serif;
    font-style: italic;
    font-size: 13px;
    letter-spacing: 1.5px;
    color: var(--ink);
  }
  .contact-list {
    position: absolute;
    left: 34px; top: 502px;
    list-style: none;
  }
  .contact-list li {
    display: flex; align-items: center;
    height: 20.5px;
    font-size: 7.5px;
    letter-spacing: 0.8px;
    color: var(--ink);
  }
  .contact-list svg {
    width: 16px; height: 14px;
    margin-right: 18px;
    fill: var(--ink);
  }
</style>
</head>
<body>

<section class="card card-front">
  <svg class="front-flap" viewBox="0 0 425 660" aria-hidden="true">
    <path d="M0 0 H425 V110 H285 A73 73 0 0 1 140 110 H0 Z" fill="var(--teal-light)"/>
    <path d="M0 110 H140 A73 73 0 0 0 285 110 H425" fill="none" stroke="#5f8f8f" stroke-width="1" stroke-dasharray="6 4"/>
    <path d="M130 110 A83 83 0 0 0 295 110" fill="none" stroke="#5f8f8f" stroke-width="1" stroke-dasharray="4 4"/>
  </svg>
  <div class="badge front-badge">VELORA<br>PAIR</div>
  <h1 class="front-name">VELORA PAIR</h1>
  <div class="front-footer">www.velorasoulpair.com</div>
</section>

<section class="card card-back">
  <div class="back-spine"></div>
  <svg class="back-tab" viewBox="0 0 76 76" aria-hidden="true">
    <path d="M0 0 H76 V54 Q76 62 68 64 L38 74 L8 64 Q0 62 0 54 Z" fill="var(--teal)"/>
  </svg>
  <div class="badge back-badge">VELORA<br>PAIR</div>

  <h2 class="tagline">CLASSIC COCKTAIL MUSIC</h2>

  <div class="person">
    <div class="person-name">MARIBEL THORNE</div>
    <div class="person-role">owner</div>
  </div>

  <ul class="contact-list">
    <li>
      <svg viewBox="0 0 16 14"><path d="M8 0 L16 7 H13.5 V14 H9.5 V9.5 H6.5 V14 H2.5 V7 H0 Z"/></svg>
      12/48 Kestrel Lane Toowong Queensland 4066 – Australia
    </li>
    <li>
      <svg viewBox="0 0 16 14"><path d="M4 0 L6.5 3.5 L5 5.2 Q6.5 8.5 9.5 10 L11 8.5 L14.5 11 L13 13.5 Q7 14 3 8 Q1 4 2 1.5 Z"/></svg>
      0437 215 964
    </li>
    <li>
      <svg viewBox="0 0 16 14"><rect x="3" y="0" width="10" height="14" rx="1.5"/></svg>
      velorapair@fernmail.com
    </li>
    <li>
      <svg viewBox="0 0 16 14"><path d="M8 0 L16 5 V14 H0 V5 Z M2 6 L8 10 L14 6 V12 H2 Z" fill-rule="evenodd"/></svg>
      www.velorasoulpair.com
    </li>
  </ul>
</section>

</body>
</html>
```